Garden Design Flier

I would like a PDF of this half page A4 flier in soft green tones with dark green leaves.

Target Market(s)

Home owners and real estate agents

Font styles to use
Serif
Other font styles liked:
• Papyrus

Colors
acd136
9bcb3c
cadf82
fefdec

Requirements
Must have
• Green tones
Nice to have
• Leaves, vines, lawns
Should not have
• Open to ideas, but classic style

```html
<!DOCTYPE html>
<html lang="en">
<head>
<meta charset="utf-8">
<title>Heirloom Gardens Flier</title>
<link rel="stylesheet" href="https://fonts.googleapis.com/css2?family=Sorts+Mill+Goudy:ital@0;1&display=swap">
<style>
  :root {
    --mint: #8ecfbe;
    --leaf: #22a98a;
    --leaf-soft: #3bb497;
    --paper: #ffffff;
  }
  html, body {
    margin: 0;
    padding: 0;
    overflow: hidden;
    background: var(--mint);
  }
  .flier {
    position: relative;
    width: 1200px;
    height: 848px;
    overflow: hidden;
    background: var(--mint);
    font-family: "Sorts Mill Goudy", Georgia, serif;
    color: var(--paper);
  }
  .frame {
    position: absolute;
    left: 0; top: 0;
    width: 1200px; height: 848px;
  }
  .art {
    position: absolute;
    left: 0; top: 0;
    width: 1200px; height: 848px;
  }
  .brand-ring {
    position: absolute;
    left: 530px; top: 86px;
    width: 138px; height: 138px;
    box-sizing: border-box;
    border: 9px solid var(--paper);
    border-radius: 50%;
  }
  .brand-name {
    position: absolute;
    left: 0; width: 1200px;
    top: 252px;
    margin: 0;
    text-align: center;
    font-weight: 400;
    font-size: 55px;
    letter-spacing: 2px;
    line-height: 1;
    padding-left: 0;
  }
  .brand-owner {
    position: absolute;
    left: 0; width: 1200px;
    top: 322px;
    margin: 0;
    text-align: center;
    font-style: italic;
    font-size: 40px;
    line-height: 1;
  }
  .services {
    position: absolute;
    left: 0; width: 1200px;
    top: 400px;
    margin: 0;
    text-align: center;
    font-size: 37px;
    line-height: 1;
    word-spacing: 6px;
  }
  .services em { font-style: italic; }
  .services .sep { padding: 0 8px; }
  .intro {
    position: absolute;
    left: 0; width: 1200px;
    top: 462px;
    margin: 0;
    text-align: center;
    font-size: 19px;
    line-height: 28px;
  }
  .contact {
    position: absolute;
    right: 100px;
    top: 668px;
    margin: 0;
    text-align: right;
    font-size: 27px;
    line-height: 36px;
    letter-spacing: 0.5px;
  }
  .credential {
    position: absolute;
    left: 81px;
    top: 703px;
    margin: 0;
    font-style: italic;
    font-size: 27px;
    line-height: 37px;
  }
  .credential .badge {
    display: inline-block;
    width: 84px; height: 22px;
    margin-left: 6px;
    background: var(--paper);
    vertical-align: -1px;
  }
</style>
</head>
<body>
<main class="flier">
  <svg class="art" viewBox="0 0 1200 848" aria-hidden="false">
    <defs>
      <linearGradient id="leafTone" x1="0" y1="0" x2="1" y2="1">
        <stop offset="0" stop-color="#22a98a"/>
        <stop offset="1" stop-color="#2cae90"/>
      </linearGradient>
    </defs>
    <path role="img" aria-label="Silhouettes of fern fronds and garden leaves trailing from the top right corner"
          fill="url(#leafTone)"
          d="M700 60 C800 30 950 28 1170 30 L1172 380 C1140 400 1090 395 1075 350 C1040 300 990 260 940 300 C900 270 880 230 860 190 C820 150 760 120 700 60 Z"/>
    <path role="img" aria-label="Silhouettes of parsley, carrot, chillies, radish and tomatoes along the lower left"
          fill="url(#leafTone)"
          d="M36 530 C90 520 170 530 250 545 C320 560 390 560 410 600 C450 640 460 680 470 720 C495 740 505 780 500 812 L36 812 Z"/>
  </svg>

  <svg class="frame" viewBox="0 0 1200 848" aria-hidden="true">
    <rect x="32" y="26" width="1138" height="794" fill="none" stroke="var(--paper)" stroke-width="9"/>
  </svg>

  <div class="brand-ring" aria-hidden="true"></div>

  <h1 class="brand-name">HEIRLOOM GARDENS</h1>
  <p class="brand-owner">by Elliot Marsh</p>

  <p class="services">Design <span class="sep">/</span> Install <span class="sep">/</span> Grow <span class="sep">/</span> Tend <span class="sep">/</span> <em>Enjoy!</em></p>

  <p class="intro">All your gardening and landscaping needs from design &amp; installation to general maintenance.<br>Bespoke vegetable gardens and potager designs created to suite your site and requirments.</p>

  <p class="credential">CERTIFICATE III<br>Horticulture.<span class="badge" aria-hidden="true"></span></p>

  <p class="contact">Email: elliot@heirloomgardens.com.au<br>Mobile: 0400 128 553<br>ABN: 51209874316</p>
</main>
</body>
</html>
```